Brightacre Preschool UI Design

**This has to be designed in landscape and NOT portrait :)
We need a user interface design for login screen we will have displayed at all times on our Tablixes in the reception area. These Tablixes will log our "Kinderquests" in and out using a login and password, and will sign them in for the day. This is a brand new, state-of-the-art 21st century learning environment. Our logo was made my a designer on artmarketly :)
We will have 2 main login screens:
one for admin
one for parents
I would like something fun and playful - and possibly "natural" looking as we are a Reggio Emilia inspired program (similar to Montessori).
Please visit our website to learn more about us:
www.Brightacre.example
I attached an example of the buttons/options we will need on the login screen - just don't think it looks great and want something more professional/sophisticated.
Thank you!
Industry/Entity Type
Landscape
Requirements
Must have
- landscape orientation

```html
<!DOCTYPE html>
<html lang="en">
<head>
<meta charset="utf-8">
<title>Brightacre Preschool – Staff Login</title>
<link href="https://fonts.googleapis.com/css2?family=Josefin+Sans:wght@300;400;600;700&display=swap" rel="stylesheet">
<style>
  :root {
    --teal-top: #54c4af;
    --teal-bottom: #45978a;
    --teal-accent: #52c0a8;
    --white: #ffffff;
    --ink-muted: #8795a4;
    --ink-soft: #a6aeb6;
    --field-border: #dadfe3;
    --icon-grey: #b4bcc3;
    --bar-ink: #222222;
    --battery: #4cd964;
  }
  * { box-sizing: border-box; margin: 0; padding: 0; }
  html, body { width: 1200px; height: 900px; overflow: hidden; }
  body { font-family: "Josefin Sans", sans-serif; background: var(--white); position: relative; }

  .status-bar {
    position: absolute; top: 0; left: 0; width: 1200px; height: 23px;
    font-size: 13px; display: flex; justify-content: space-between; align-items: center;
    padding: 0 8px; z-index: 2; color: var(--white);
  }
  .status-bar .carrier { display: flex; align-items: center; gap: 4px; }
  .status-bar .clock { position: absolute; left: 600px; font-weight: 600; }
  .status-bar .battery { color: var(--bar-ink); display: flex; align-items: center; gap: 4px; }

  .welcome-panel {
    position: absolute; top: 0; left: 0; width: 637px; height: 900px;
    background: linear-gradient(180deg, var(--teal-top) 0%, var(--teal-accent) 45%, var(--teal-bottom) 100%);
    color: var(--white);
  }
  .hero-art {
    position: absolute; left: 72px; top: 182px; width: 485px; height: 452px;
    border-radius: 40% 40% 48% 48% / 30% 30% 12% 12%;
    background: radial-gradient(ellipse at 50% 55%, rgba(255,255,255,0.18), rgba(255,255,255,0.04) 70%, transparent 75%);
  }
  .school-name {
    position: absolute; left: 59px; top: 716px;
    font-size: 56px; font-weight: 700; letter-spacing: 2px; line-height: 1;
  }
  .opening-note {
    position: absolute; left: 59px; top: 786px;
    font-size: 33px; font-weight: 300; line-height: 1;
  }

  .login-panel { position: absolute; top: 0; left: 637px; width: 563px; height: 900px; }
  .brand-mark {
    position: absolute; left: 0; width: 563px; top: 182px;
    display: flex; align-items: center; justify-content: center; gap: 12px;
    color: var(--ink-muted); font-size: 26px; font-weight: 600; letter-spacing: 1px;
  }
  .brand-mark .dot { width: 22px; height: 22px; border-radius: 50%; background: var(--teal-accent); }
  .login-title {
    position: absolute; left: 0; width: 563px; top: 328px; text-align: center;
    font-size: 27px; font-weight: 400; color: var(--ink-muted);
  }
  .field {
    position: absolute; left: 118px; width: 327px; height: 55px;
    border: 1px solid var(--field-border); border-radius: 3px;
    display: flex; align-items: center; padding: 0 16px; gap: 16px;
    color: var(--ink-soft); font-size: 17px;
  }
  .field.username { top: 405px; }
  .field.password { top: 484px; }
  .field .label { flex: 1; padding-top: 3px; }
  .forgot-link {
    position: absolute; left: 118px; top: 582px; font-size: 17px; color: var(--ink-soft);
  }
  .login-button {
    position: absolute; left: 282px; top: 564px; width: 163px; height: 55px;
    background: var(--teal-accent); color: var(--white); border-radius: 3px;
    display: flex; align-items: center; justify-content: center;
    font-size: 16px; font-weight: 700; letter-spacing: 0.5px; padding-top: 3px;
    box-shadow: 0 6px 14px rgba(82,192,168,0.35);
  }
  .footer-link {
    position: absolute; top: 744px; display: flex; align-items: center; gap: 7px;
    color: var(--teal-accent); font-size: 18px;
  }
  .footer-link.home { left: 118px; }
  .footer-link.parents { right: 118px; }
</style>
</head>
<body>
  <div class="status-bar">
    <span class="carrier">●●○○○ Slate
      <svg width="14" height="10" viewBox="0 0 14 10"><path d="M7 9 1 3a8.5 8.5 0 0 1 12 0z" fill="currentColor"/></svg>
    </span>
    <span class="clock">9:41 AM</span>
    <span class="battery">100%
      <svg width="30" height="12" viewBox="0 0 30 12"><rect x="0.5" y="0.5" width="25" height="11" rx="2" fill="none" stroke="#222"/><rect x="2" y="2" width="22" height="8" rx="1" fill="var(--battery)"/><rect x="26.5" y="4" width="2" height="4" fill="#222"/></svg>
    </span>
  </div>

  <section class="welcome-panel">
    <div class="hero-art" role="img" aria-label="Illustration of two cheerful schoolchildren beside a giant red book and a tall yellow pencil"></div>
    <h1 class="school-name">BRIGHTACRE</h1>
    <p class="opening-note">Opening in january 2018</p>
  </section>

  <section class="login-panel">
    <div class="brand-mark"><span class="dot"></span>Brightacre</div>
    <h2 class="login-title">Only for Brightacre Staff</h2>

    <div class="field username">
      <svg width="18" height="18" viewBox="0 0 18 18" fill="var(--icon-grey)"><circle cx="9" cy="5" r="4"/><path d="M1 17c0-4 3.5-6.5 8-6.5s8 2.5 8 6.5z"/></svg>
      <span class="label">Username</span>
    </div>
    <div class="field password">
      <svg width="18" height="18" viewBox="0 0 18 18" fill="var(--icon-grey)"><circle cx="12" cy="6" r="5"/><path d="M8 9 1 16l1.5 1.5 1.5-1.5 1.5 1.5 1.5-1.5-1.5-1.5L10 10.5z"/></svg>
      <span class="label">Password</span>
      <svg width="18" height="12" viewBox="0 0 18 12" fill="var(--icon-grey)"><path d="M9 0C5 0 2 3 0 6c2 3 5 6 9 6s7-3 9-6c-2-3-5-6-9-6zm0 10a4 4 0 1 1 0-8 4 4 0 0 1 0 8z"/><circle cx="9" cy="6" r="2"/></svg>
    </div>

    <a class="forgot-link">Forgot Password?</a>
    <div class="login-button">STAFF LOGIN</div>

    <a class="footer-link home">
      <svg width="20" height="18" viewBox="0 0 20 18" fill="currentColor"><path d="M10 0 0 9h3v9h5v-6h4v6h5V9h3z"/></svg>
      Go to Home
    </a>
    <a class="footer-link parents">
      <svg width="22" height="18" viewBox="0 0 22 18" fill="currentColor"><circle cx="8" cy="5" r="4"/><path d="M0 17c0-4 3.5-6 8-6s8 2 8 6z"/><circle cx="16" cy="5" r="3"/><path d="M15 10.5c4 0 7 2 7 6.5h-4.5c0-2.5-1-4.5-2.5-6.5z"/></svg>
      Parents Login
    </a>
  </section>
</body>
</html>
```